Brent's Business Cards

My husband is a self employed Cabinet Maker... who contracts to Building companies and clients directly.
He installs kitchesn, designs and also completes renovations and building work.

I would like a small, FUNKY, simple but eye catching design.

It needs to incorporate the following.
Custom Cabinets / Installations / Renovations / Design

Commercial and Residential

He does not have a Website or Facebook,
contact number is 0438 207 964 and email is brentkelway@mailpost.example

I would like a Grey/Silver on black, or blue covering.. I am open to colour designs?

Thank you. :-)

Target Market(s)

Building Companies
Clients
Other Trades people onsite,. to give out at job sites

Industry/Entity Type

Business

Contact Information for Business Card

Phone: 0438 207 964
Email: brentkelway@mailpost.example

Font styles to use
Sans Serif

Colors
0592cd
747474
474747
1b1b1b
85cae6

Requirements
Must have
• Funky, simple, eye catching design
• Would like use of Silver/Grey - and a colour that would complement this.
• Am open to ideas :-)
Nice to have
• We do not have a logo or picture, will leave this up to you if you think an image would be beneficial???
• Thank you.

Files

```html
<!DOCTYPE html>
<html lang="en">
<head>
<meta charset="UTF-8">
<title>Brent Kelway – Cabinet Maker Business Card</title>
<link rel="stylesheet" href="https://fonts.googleapis.com/css2?family=Exo+2:wght@700&family=Lato:wght@400;700;900&display=swap">
<style>
  :root {
    --ink-black: #1b1b1b;
    --charcoal: #474747;
    --steel-grey: #747474;
    --brand-blue: #0592cd;
    --sky-blue: #85cae6;
    --card-white: #ffffff;
    --backdrop: #e4e4e4;
  }
  * { box-sizing: border-box; margin: 0; padding: 0; }
  html, body {
    width: 1200px; height: 800px; overflow: hidden;
    background: var(--backdrop);
  }
  .stage {
    width: 1200px; height: 800px;
    display: flex; align-items: center; justify-content: center;
  }
  .business-card {
    position: relative;
    width: 400px; height: 700px;
    background: var(--card-white);
    box-shadow: 0 6px 22px rgba(0,0,0,0.14);
    overflow: hidden;
    font-family: "Lato", Arial, sans-serif;
  }
  .card-edges { position: absolute; inset: 0; }
  .name-block {
    position: absolute; left: 0; right: 0; top: 138px;
    text-align: center; color: var(--card-white);
  }
  .owner-name {
    font-family: "Exo 2", "Arial Black", sans-serif;
    font-weight: 700; font-size: 40px; letter-spacing: 0.5px;
    line-height: 1;
  }
  .owner-title {
    display: block; text-align: right;
    padding-right: 44px; margin-top: 4px;
    font-size: 15px; font-weight: 400; color: #e6e6e6;
  }
  .services {
    position: absolute; left: 38px; right: 38px; top: 286px;
  }
  .services-heading {
    font-weight: 900; font-size: 17px; letter-spacing: 0.3px;
    color: var(--charcoal); text-transform: uppercase;
    padding-bottom: 10px;
    border-bottom: 2px solid var(--steel-grey);
  }
  .services-list {
    margin-top: 10px;
    font-size: 16px; line-height: 1.3; color: var(--steel-grey);
    padding-bottom: 16px;
    border-bottom: 1px solid #9a9a9a;
  }
  .contact-list {
    position: absolute; left: 38px; right: 38px; top: 428px;
    list-style: none;
    border-bottom: 1.5px solid var(--charcoal);
    padding-bottom: 20px;
  }
  .contact-item {
    display: flex; align-items: center; gap: 16px;
    margin-bottom: 22px;
    font-size: 17px; color: var(--charcoal);
  }
  .contact-item:last-child { margin-bottom: 0; }
  .contact-item.address { line-height: 1.25; }
  .contact-icon { width: 24px; height: 24px; flex: none; }
</style>
</head>
<body>
<main class="stage">
  <article class="business-card">
    <svg class="card-edges" width="400" height="700" viewBox="0 0 400 700" aria-hidden="true">
      <defs>
        <linearGradient id="top-sheen" x1="0" y1="0" x2="1" y2="1">
          <stop offset="0" stop-color="#2c2c2c"/>
          <stop offset="1" stop-color="var(--ink-black)"/>
        </linearGradient>
      </defs>
      <polygon class="header-band" fill="url(#top-sheen)"
        points="0,0 400,0 400,235 390,253 380,235 370,253 360,235 350,253 340,235 330,253 320,235 310,253 300,235 290,253 280,235 270,253 260,235 250,253 240,235 230,253 220,235 210,253 200,235 190,253 180,235 170,253 160,235 150,253 140,235 130,253 120,235 110,253 100,235 90,253 80,235 70,253 60,235 50,253 40,235 30,253 20,235 10,253 0,235"/>
      <polygon class="footer-band" fill="var(--brand-blue)"
        points="0,700 0,631 10,612 20,631 30,612 40,631 50,612 60,631 70,612 80,631 90,612 100,631 110,612 120,631 130,612 140,631 150,612 160,631 170,612 180,631 190,612 200,631 210,612 220,631 230,612 240,631 250,612 260,631 270,612 280,631 290,612 300,631 310,612 320,631 330,612 340,631 350,612 360,631 370,612 380,631 390,612 400,631 400,700"/>
    </svg>

    <header class="name-block">
      <h1 class="owner-name">BRENT KELWAY</h1>
      <span class="owner-title">Cabinet Maker</span>
    </header>

    <section class="services">
      <h2 class="services-heading">Commercial and Residential</h2>
      <p class="services-list">Custom Cabinets / Installations /<br>Renovations / Design</p>
    </section>

    <ul class="contact-list">
      <li class="contact-item phone">
        <svg class="contact-icon" viewBox="0 0 24 24" aria-hidden="true">
          <path d="M6.5 3.5l3 3.2-1.8 2.1c1.2 2.5 3 4.3 5.5 5.5l2.1-1.8 3.2 3-1.6 3.2c-7.2-.4-13.2-6.4-13.6-13.6z" fill="var(--charcoal)"/>
        </svg>
        <span>0438 207 964</span>
      </li>
      <li class="contact-item email">
        <svg class="contact-icon" viewBox="0 0 24 24" aria-hidden="true">
          <rect x="2" y="5" width="20" height="14" fill="var(--charcoal)"/>
          <polyline points="2,5 12,13 22,5" fill="none" stroke="#fff" stroke-width="1.6"/>
        </svg>
        <span>brentkelway@mailpost.example</span>
      </li>
      <li class="contact-item address">
        <svg class="contact-icon" viewBox="0 0 24 24" aria-hidden="true">
          <circle cx="12" cy="12" r="10" fill="none" stroke="var(--ink-black)" stroke-width="2"/>
          <polygon points="16.5,7.5 13.2,13.2 10.8,10.8" fill="var(--ink-black)"/>
          <polygon points="7.5,16.5 10.8,10.8 13.2,13.2" fill="var(--steel-grey)"/>
        </svg>
        <span>48 Harbour Lane,<br>Rivermount 3870</span>
      </li>
    </ul>
  </article>
</main>
</body>
</html>
```